Catalogue Design Project

We require a new 2013 catalogue cover designed ( front & back with a one inch wide spine) for our business, Brellow Office Supplies. We have been established for 36 years and we supply all sorts of companies across the UK with a Variety of Office Stationery, Computer Products, Print, Furniture, Catering and Cleaning products within the UK - you can browse our catalogue on our website www.brellow.co.uk - using test as both user id and password.
We are serious about customer service; ensure we do the very best for our clients with the best prices. For us it’s all about the image we portray to our clients, we don’t want the cover to look like it’s the cover of a Yacht catalogue, nor do we want it to look like a trashy magazine.
The main priority of this design is that the Catalogue looks professional and appealing. Good use of colour, possibly incorporating elements of what we do would be of advantage.
(Please visit our website www.brellow.co.uk for details).
The Catalogue is to be A4 in size, MUST have our company logo in on the front, which we will supply, but for the start obtainable from our site)
The Catalogue covers will have insides both front and back that we will be printing on. Your design and use of colours should be able to flow onto these pages so as we can print on a continuation of your design.
**UPDATE - Please note the content is already designed, this is for the front/back cover and inside covers**
There will be a few edits after we make a choice...
if you need anything from us then please email us on jpike@brellow.co.uk
Best of luck
PROJECT NOW GUARANTEED.!!
Due to the High Quality of designs being submitted - we are now happy to commit to one of you! Keep the designs coming!
Good Luck!
The Buyers of our products are corporate companies
Printing

```html
<!DOCTYPE html>
<html lang="en">
<head>
<meta charset="utf-8">
<title>Brellow Office Supplies – Inside Covers</title>
<link rel="stylesheet" href="https://fonts.googleapis.com/css2?family=Bebas+Neue&family=Open+Sans:wght@300;400;700&display=swap">
<style>
  :root {
    --stage-blue: #1b88b6;
    --cover-yellow: #ffd600;
    --cover-grey: #b6b6b8;
    --ink: #1d1d1b;
    --label-white: #ffffff;
    --edge-dark: #2a2a2a;
  }
  * { margin: 0; padding: 0; box-sizing: border-box; }
  html, body {
    width: 1200px;
    height: 850px;
    overflow: hidden;
    background: var(--stage-blue);
  }
  .spread {
    position: relative;
    width: 1200px;
    height: 850px;
    font-family: "Open Sans", Arial, sans-serif;
    color: var(--ink);
  }
  .page {
    position: absolute;
    top: 31px;
    height: 753px;
    border-bottom: 2px solid var(--edge-dark);
  }
  .page--front-inside {
    left: 37px;
    width: 562px;
    background: var(--cover-yellow);
  }
  .page--back-inside {
    left: 599px;
    width: 564px;
    background: var(--cover-grey);
  }
  .products {
    position: absolute;
    left: 31px;
    top: 181px;
    width: 476px;
  }
  .products__title {
    font-weight: 300;
    font-size: 26px;
    line-height: 1.2;
    margin-bottom: 14px;
  }
  .products__intro {
    font-size: 11.6px;
    line-height: 15px;
    text-align: justify;
    margin-bottom: 15px;
  }
  .products__list {
    list-style: none;
    margin-top: 27px;
  }
  .products__item {
    font-weight: 700;
    font-size: 12.4px;
    line-height: 26.8px;
  }
  .web-address {
    position: absolute;
    top: 378px;
    left: 0;
    width: 100%;
    text-align: center;
    font-weight: 700;
    font-size: 16px;
  }
  .page-label {
    position: absolute;
    top: 805px;
    font-family: "Bebas Neue", Impact, sans-serif;
    font-size: 29px;
    color: var(--label-white);
    letter-spacing: 0.5px;
    transform: translateX(-50%);
    white-space: nowrap;
  }
  .page-label--front { left: 268px; }
  .page-label--back { left: 937px; }
</style>
</head>
<body>
<main class="spread">
  <section class="page page--front-inside">
    <div class="products">
      <h1 class="products__title">Our Products</h1>
      <p class="products__intro">With over 100,000 product lines within our catalogue the products available to you for the Next Day are vast……</p>
      <p class="products__intro">Below we have shown a slight drill down into the product categories that we can supply you with, it is not an extensive list but should help you to see that we aim to be able to provide you with all the products that you may need in order to keep your office running.</p>
      <ul class="products__list">
        <li class="products__item">Office Stationery</li>
        <li class="products__item">Legal Supplies</li>
        <li class="products__item">Business Machines &amp; IT Consumable</li>
        <li class="products__item">Office Furniture &amp; Seating</li>
        <li class="products__item">Facilities Management &amp; Catering</li>
        <li class="products__item">Print</li>
        <li class="products__item">Product Sourcing</li>
      </ul>
    </div>
  </section>
  <section class="page page--back-inside">
    <p class="web-address">www.brellow.co.uk</p>
  </section>
  <p class="page-label page-label--front">Front Inside</p>
  <p class="page-label page-label--back">Back Inside</p>
</main>
</body>
</html>
```